Looking for a unique designer to design new & exciting stationery for progressive professional firm

Hello! We would like to stand out, but in a good way. We want a modern unique image, something creative, but remain professional. Also portray integrity and look approachable. We want to appeal to the younger generation while not losing the respect of our more conservative older clients!

Our focus at Lantern Partners is on guiding our clients and assisting them to 'keep your books in order'. We are a small boutique accounting firm based in Melbourne Australia.

Using our 2 distinctive colours (blue & yellow) and new logo design attached, please design a modern and professional letterhead, with compliments slip and business card for our firm.

The necessary words and logos to be included on the letterhead and card are attached, the overall design of the stationery however is up to your talent. Font to be modern, professional & progressive! I like the font style (MS words Trebuchet MS) on my draft letterhead design attached. It looks modern, professional but approachable so something like that would be great.

For the business card, I like the attached version's REAR side of the business card but not the front side, so please come up with a design for the front that will match the letterhead design you come up with. I don't like how the company name sits tightly below the logo, they make the logo look too large in proportion to the words. Also feel free to change the rear side if you believe you have a better design :)

The colours are blue R31 G125 B165
and yellow R224 G201 B24, but please convert to CMYK equivalent.

At full sizing for the card, withcomps slip and letterhead respectively, the images need to be at least 300 dpi or higher.

Please advise if you need any other files (eg for higher resolution) or information and/or refer to our website for further input.

Thank you, with great anticipation...

Dylan

Target Market(s)

Discerning (and wealthy?) clients, both business owners and personal, looking for a progressive, approachable but professional accounting firm. Need to attract and appeal to the younger generations while not losing the respect of the older more conservative generation.

Industry/Entity Type

Accounting

Font styles to use
Other font styles liked:
• Something like MW word's Trebuchet MS - for company name. Happy for you to suggest other font for other wording.

Requirements
Must have
• My company logo, QBT logo, the wording I have included on the sample of letterhead and business card.
• The colours are blue R31 G125 B165 and yellow R224 G201 B24, but please convert to CMYK equivalent. Also use a grey for smaller wording. Refer sample letterhead attached. Note that the blue and yellow on the QBT logo are not the same as the my blue and yellow above. They will and should look different.
• Note: QBT logo must have a space around it of at least half the width of the yellow part of the logo - per my attached letter sample. The logo must be at least 15mm in width on all stationery. Also the QBT logo must have the words adjacent to it, 'Lantern Partners Pty Ltd is a QBT practice'.
Nice to have
• Maybe curved features at bottom and/or top of letterhead instead of the rectangle coloured bars that my sample letter has.
• Good to maybe have Icons for telephone, fax email address etc.
Should not have
• No other colours except my blue, yellow and black, grey and white.
• No detailed pictures as I want to keep the design modern, minimalistic and flat.

```html
<!DOCTYPE html>
<html lang="en">
<head>
<meta charset="utf-8">
<title>Lantern Partners – Letterhead</title>
<link rel="stylesheet" href="https://fonts.googleapis.com/css2?family=Lato:ital,wght@0,400;0,700;1,400&family=PT+Sans&display=swap">
<style>
  :root {
    --brand-blue: #1f7da5;
    --brand-yellow: #e0c918;
    --tagline-olive: #a89616;
    --text-grey: #555555;
    --text-dark: #222222;
    --paper: #f5f4f2;
    --backdrop: #a9a8a8;
  }
  * { margin: 0; padding: 0; box-sizing: border-box; }
  html, body {
    width: 938px; height: 1200px; overflow: hidden;
    background: var(--backdrop);
  }
  .letterhead {
    position: absolute; left: 81px; top: 53px;
    width: 776px; height: 1094px;
    background: var(--paper);
    font-family: "Lato", sans-serif;
    overflow: hidden;
  }
  .brand {
    position: absolute; left: 38px; top: 33px; width: 200px;
    text-align: center;
    font-family: "PT Sans", sans-serif;
  }
  .brand-dot {
    display: block; width: 56px; height: 56px; margin: 0 auto 9px;
    border-radius: 50%; background: var(--brand-yellow);
  }
  .brand-name {
    color: var(--brand-blue); font-size: 19.5px; line-height: 20px;
    letter-spacing: 0.2px; text-transform: uppercase;
  }
  .brand-tagline {
    color: var(--tagline-olive); font-size: 11.5px; line-height: 15px;
  }
  .practice {
    position: absolute; right: 37px; top: 35px; text-align: right;
  }
  .practice-badge {
    display: block; width: 49px; height: 20px; margin: 0 0 8px auto;
    background: var(--brand-blue);
  }
  .practice-entity {
    color: var(--brand-blue); font-weight: 700; font-size: 7px;
    line-height: 9.5px; text-transform: uppercase;
  }
  .practice-liability {
    margin-top: 3px; color: var(--text-grey); font-style: italic;
    font-size: 8.5px; line-height: 11px;
  }
  .practice-principal {
    color: var(--brand-blue); font-size: 8.5px; line-height: 12px;
  }
  .footer-details {
    position: absolute; left: 0; right: 0; top: 1016px;
    text-align: center; color: var(--text-grey);
    font-size: 8.6px; line-height: 13px;
    z-index: 2;
  }
  .footer-details strong { color: var(--text-dark); font-weight: 400; }
  .footer-details .label { color: var(--brand-blue); font-weight: 700; }
  .footer-wave {
    position: absolute; left: 0; bottom: 0; width: 776px; height: 74px;
    z-index: 1;
  }
</style>
</head>
<body>
  <main class="letterhead">
    <header class="brand">
      <span class="brand-dot"></span>
      <p class="brand-name">Lantern Partners</p>
      <p class="brand-tagline">Keep your books in order</p>
    </header>

    <aside class="practice">
      <span class="practice-badge"></span>
      <p class="practice-entity">Lantern Partners Pty Ltd<br>is a QBT practice</p>
      <p class="practice-liability">Liability limited by a scheme approved under<br>Professional Standards Legislation</p>
      <p class="practice-principal">Dylan A Harrow&nbsp; BBus, QBT, RTA</p>
    </aside>

    <svg class="footer-wave" viewBox="0 0 776 74" aria-hidden="true">
      <path d="M0 7 C150 55 450 62 776 21 L776 23 C450 74 150 66 0 23 Z" fill="var(--brand-yellow)"/>
      <path d="M0 26 C150 70 450 78 776 25 L776 74 L0 74 Z" fill="var(--brand-blue)"/>
    </svg>

    <footer class="footer-details">
      <p>ABN 12 345 678 901</p>
      <p><strong>Accountants &amp; Business Advisors,</strong> Suite 12,&nbsp; 48 Ferncliff Road, Ashvale&nbsp; Victoria&nbsp; 3150</p>
      <p><span class="label">P :</span> +61 3 9000 1234&nbsp; <span class="label">F :</span> +61 3 9000 1235&nbsp; <span class="label">E :</span> info@lanternpartners.example&nbsp; <span class="label">W :</span> www.lanternpartners.example</p>
    </footer>
  </main>
</body>
</html>
```